Typing Service Business Card Design

Need a new business card design for new logo update. The Ledger Scribes is an outsourced typing service. We type audio / voice files into word documents. We are a professional service that is recognised in the industry over the past 15 years and have a strong connection to our brand. The final design should be professional, simple, yet effective.

Corinna Waldrop
Director

corinna@lsx.com.au
www.theledgerscribes.com.au

```html
<!DOCTYPE html>
<html lang="en">
<head>
<meta charset="utf-8">
<title>The Ledger Scribes — Business Card</title>
<link rel="stylesheet" href="https://fonts.googleapis.com/css2?family=Mulish:wght@400;600&display=swap">
<style>
  :root {
    --backdrop: #4a4a4a;
    --card-light: #ffffff;
    --card-dark: #232121;
    --brand-pink: #d1459a;
    --ink: #2b2b2b;
    --ink-soft: #555555;
    --paper-white: #ffffff;
    --muted-light: #bdbdbd;
  }
  * { margin: 0; padding: 0; box-sizing: border-box; }
  html, body {
    width: 1105px;
    height: 1200px;
    overflow: hidden;
    background: var(--backdrop);
    font-family: "Mulish", sans-serif;
  }
  .card {
    position: absolute;
    left: 196px;
    width: 720px;
    height: 412px;
    box-shadow: 0 4px 10px rgba(0,0,0,0.35);
  }
  .card--front { top: 146px; background: var(--card-light); }
  .card--back  { top: 602px; background: var(--card-dark); }

  .brand {
    position: absolute;
    display: flex;
    flex-direction: column;
  }
  .card--front .brand { right: 36px; top: 66px; align-items: flex-end; }
  .card--back .brand { left: 50%; top: 172px; transform: translateX(-50%); align-items: center; }

  .brand__lockup {
    display: flex;
    align-items: center;
    gap: 14px;
  }
  .brand__mark {
    width: 22px;
    height: 22px;
    background: var(--brand-pink);
  }
  .brand__name {
    font-weight: 600;
    font-size: 30px;
    color: var(--ink);
    white-space: nowrap;
    line-height: 1;
  }
  .card--back .brand__name { color: var(--paper-white); }

  .brand__tagline {
    font-size: 16px;
    font-weight: 400;
    letter-spacing: 2px;
    text-transform: uppercase;
    margin-top: 14px;
    color: var(--ink-soft);
    line-height: 1;
  }
  .card--back .brand__tagline { color: var(--muted-light); }

  .contact-block {
    position: absolute;
    left: 36px;
    top: 252px;
  }
  .person__name {
    font-weight: 600;
    font-size: 27px;
    color: var(--brand-pink);
    letter-spacing: 0.5px;
    line-height: 1.1;
  }
  .person__role {
    font-size: 19px;
    color: var(--ink);
    letter-spacing: 0.6px;
    margin-top: 2px;
  }
  .contact-list {
    list-style: none;
    margin-top: 16px;
  }
  .contact-list__item {
    display: flex;
    align-items: center;
    font-size: 19px;
    color: var(--ink-soft);
    letter-spacing: 0.4px;
    line-height: 28px;
  }
  .contact-list__icon {
    width: 17px;
    height: 17px;
    margin-right: 12px;
    flex: none;
  }
</style>
</head>
<body>
  <section class="card card--front">
    <div class="brand">
      <div class="brand__lockup">
        <span class="brand__mark" aria-hidden="true"></span>
        <span class="brand__name">The Ledger Scribes</span>
      </div>
      <span class="brand__tagline">Every word, on record.</span>
    </div>
    <div class="contact-block">
      <p class="person__name">Corinna Waldrop</p>
      <p class="person__role">Director</p>
      <ul class="contact-list">
        <li class="contact-list__item">
          <svg class="contact-list__icon" viewBox="0 0 18 18" aria-hidden="true">
            <rect x="1" y="4" width="16" height="11" fill="var(--brand-pink)"/>
            <path d="M1.5 4.5L9 10l7.5-5.5" fill="none" stroke="#fff" stroke-width="1.4"/>
          </svg>
          corinna@lsx.com.au
        </li>
        <li class="contact-list__item">
          <svg class="contact-list__icon" viewBox="0 0 18 18" aria-hidden="true">
            <circle cx="9" cy="9" r="8" fill="var(--brand-pink)"/>
            <ellipse cx="9" cy="9" rx="3.5" ry="7.5" fill="none" stroke="#fff" stroke-width="1.2"/>
            <path d="M1.5 9h15" stroke="#fff" stroke-width="1.2"/>
          </svg>
          theledgerscribes.com.au
        </li>
      </ul>
    </div>
  </section>

  <section class="card card--back">
    <div class="brand">
      <div class="brand__lockup">
        <span class="brand__mark" aria-hidden="true"></span>
        <span class="brand__name">The Ledger Scribes</span>
      </div>
      <span class="brand__tagline">Every word, on record.</span>
    </div>
  </section>
</body>
</html>
```